Financial Advisor Resource Firm needs business card design

Need business card design for company in Omaha NE called Tallowbrook Partners. We provide resources to financial advisors....workshop programs, retirement analysis, and insurance planning. I would like to see designs that use grays, greens, black, and white colors. The final design should communicate 'collaboration' and be simple yet attractive to financial planning clients. I will attached our logo and another picture of a puzzle piece coming together. I would like the incorporate the puzzle picture somehow, maybe on the back somehow, with color or just the gray scale....OR, the picture be the front of the card with 'Tallowbrook' definition on it (see upload) and then company logo, employee name, title, address on the back (see ppt uploaded). The following disclosure needs to be included somewhere- Advisory services offered through Marlowe Ridge Advisors, LLC.
Updates

I uploaded a svg and ai file of the logo

Target Market(s)

Financial planning clients and financial advisors....so pretty diverse age range of about 40-70.

Industry/Entity Type

Financial Planning

Contact Information for Business Card

Dennis K. Holloway, MBA
Founder/President
5727 E. Larkspur Avenue
Suite 418
Omaha, NE 68297
Phone- (402) 555-0147
Cell- (402) 555-0183
Fax- (402) 555-0129
email- dennis@tallowbrookgroup.example
web address- www.tallowbrookgroup.example

Colors
1b1b1b
474747
d3d3d3
ffffff
9bcb3c
abd036

Requirements
Must have
• Must include logo provided, must be 2 sided, and must have disclosure...all of these items listed in project description

```html
<!DOCTYPE html>
<html lang="en">
<head>
<meta charset="utf-8">
<title>Tallowbrook Partners – Business Card</title>
<link href="https://fonts.googleapis.com/css2?family=Poppins:wght@300;400;500;600;700&display=swap" rel="stylesheet">
<style>
  :root {
    --ink: #1b1b1b;
    --charcoal: #474747;
    --silver: #d3d3d3;
    --white: #ffffff;
    --green: #9bcb3c;
    --lime: #abd036;
    --stage: #e9e9e9;
  }
  * { box-sizing: border-box; margin: 0; padding: 0; }
  html, body { width: 1200px; height: 870px; overflow: hidden; }
  body {
    background: var(--stage);
    font-family: "Poppins", sans-serif;
    display: flex;
    flex-direction: column;
    align-items: center;
    justify-content: center;
    gap: 30px;
  }
  .card {
    position: relative;
    width: 700px;
    height: 400px;
    border-radius: 16px;
    overflow: hidden;
    box-shadow: 0 6px 18px rgba(0,0,0,.18);
  }
  .card-art { position: absolute; inset: 0; width: 100%; height: 100%; }

  /* back */
  .back-logo {
    position: absolute;
    left: 0; right: 0; top: 170px;
    display: flex; align-items: center; justify-content: center; gap: 12px;
  }
  .logo-dot { width: 16px; height: 16px; border-radius: 50%; background: var(--green); }
  .logo-name {
    font-weight: 600; font-size: 30px; letter-spacing: 2px; text-transform: uppercase;
  }
  .back .logo-name { color: var(--white); }
  .back-web {
    position: absolute; left: 0; right: 0; bottom: 46px; text-align: center;
    color: var(--silver); font-size: 14px; font-weight: 400; letter-spacing: .3px;
  }
  .disclosure {
    position: absolute; left: 0; right: 0; bottom: 20px; text-align: center;
    color: var(--silver); font-size: 10px; font-weight: 300; letter-spacing: .2px; opacity: .85;
  }

  /* front */
  .front { background: var(--white); }
  .identity { position: absolute; left: 40px; top: 34px; }
  .identity::before {
    content: ""; position: absolute; left: -40px; top: 2px;
    width: 26px; height: 22px; background: var(--green);
  }
  .person-name { color: var(--green); font-weight: 600; font-size: 19px; text-transform: uppercase; letter-spacing: .3px; }
  .person-title { color: var(--charcoal); font-size: 14px; font-weight: 400; margin-top: 2px; }
  .front-logo {
    position: absolute; right: 34px; top: 52px;
    display: flex; align-items: center; gap: 8px;
  }
  .front .logo-name { color: var(--ink); font-size: 20px; letter-spacing: 1.5px; }
  .front .logo-dot { width: 12px; height: 12px; }

  .contact-list {
    position: absolute; left: 34px; top: 252px; list-style: none;
    color: var(--white); font-size: 13.5px; font-weight: 300; line-height: 25px;
  }
  .contact-list li { display: flex; align-items: center; gap: 12px; }
  .contact-icon { width: 13px; height: 13px; border-radius: 50%; background: var(--green); flex: none; }
  .contact-list .web { color: var(--green); }

  .office {
    position: absolute; left: 520px; top: 290px;
    color: var(--white); font-size: 13.5px; font-weight: 300; line-height: 22px;
    font-style: normal;
  }
  .office-name { color: var(--green); font-weight: 600; }
</style>
</head>
<body>

  <section class="card back">
    <svg class="card-art" viewBox="0 0 700 400" role="img" aria-label="Grayscale photo of hands bringing puzzle pieces together">
      <defs>
        <radialGradient id="backPhoto" cx="0.55" cy="0.35" r="0.9">
          <stop offset="0" stop-color="#5a5a5a"/>
          <stop offset="0.55" stop-color="#383838"/>
          <stop offset="1" stop-color="#1b1b1b"/>
        </radialGradient>
      </defs>
      <rect width="700" height="400" fill="url(#backPhoto)"/>
    </svg>
    <div class="back-logo">
      <span class="logo-dot"></span>
      <span class="logo-name">Tallowbrook Partners</span>
    </div>
    <p class="back-web">www.tallowbrookgroup.example</p>
    <p class="disclosure">Advisory services offered through Marlowe Ridge Advisors, LLC.</p>
  </section>

  <section class="card front">
    <svg class="card-art" viewBox="0 0 700 400">
      <defs>
        <linearGradient id="frontPhoto" x1="0" y1="0" x2="1" y2="1">
          <stop offset="0" stop-color="#3f3f3f"/>
          <stop offset="0.5" stop-color="#2c2c2c"/>
          <stop offset="1" stop-color="#1b1b1b"/>
        </linearGradient>
      </defs>
      <path class="wave-gray" d="M0,186 C180,168 300,262 460,262 C560,262 640,232 700,220 L700,240 C640,252 560,284 460,286 C300,290 180,196 0,212 Z" fill="var(--silver)"/>
      <path class="wave-green" d="M0,204 C180,186 300,282 460,282 C560,282 640,250 700,238" fill="none" stroke="var(--green)" stroke-width="5"/>
      <path class="wave-photo" role="img" aria-label="Grayscale photo of hands bringing puzzle pieces together" d="M0,214 C180,196 300,292 460,292 C560,292 640,260 700,248 L700,400 L0,400 Z" fill="url(#frontPhoto)"/>
    </svg>

    <div class="identity">
      <h1 class="person-name">Dennis K. Holloway, MBA</h1>
      <p class="person-title">Founder / President</p>
    </div>

    <div class="front-logo">
      <span class="logo-dot"></span>
      <span class="logo-name">Tallowbrook Partners</span>
    </div>

    <ul class="contact-list">
      <li><span class="contact-icon"></span>(402) 555-0147</li>
      <li><span class="contact-icon"></span>(402) 555-0183</li>
      <li><span class="contact-icon"></span>(402) 555-0129</li>
      <li><span class="contact-icon"></span>dennis@tallowbrookgroup.example</li>
      <li class="web"><span class="contact-icon"></span>www.tallowbrookgroup.example</li>
    </ul>

    <address class="office">
      <div class="office-name">Tallowbrook Group</div>
      <div>5727 E. Larkspur Avenue</div>
      <div>Suite 418</div>
      <div>Omaha, NE 68297</div>
    </address>
  </section>

</body>
</html>
```